App for Lawyers & Accountants needs 'Professional' Styling

We want to style our app to convey a 'Professional' appearance. It's used by Lawyers, Accountants, Doctors etc. who take their work very seriously.

We currently trying to follow corvane layout guidelines, but we find our app looks very bland. I've uploaded a screenshot of our current app, and two mock-ups of more stylized versions, but we're not happy with those mock-ups.

We'd like to see alternate designs for those two mock-ups, that look much more professional.

The specific elements we'd like to improve/focus on are:
* Colour of the top and left nav bars
* Appearance of the left nav, size, icons spacing
* Appearance of the buttons on the top right, so the user knows they are buttons they can press
* Spacing of the dashboard, background colour and spacing, colour/layout of the 'overdue' and 'todo' accordion headings in the 'my tasks' section.
* List view background grey, to be consistent with dashboard, but unobtrusive
* List view tabs to be obvious as tabs, but 'saved searches', filters and the export icon to still be associated with the data displayed, but it should be obvious to the user that those are different buttons, not just more tabs. (I.e. the filters button opens a panel below it that allows the user to filter the data in the list.)
* General appearance of the popup menu when you push the 'add' button on the top right

However, despite those specifics I'm sure it's all the subtle elements of the design that make a big difference.

Our brand colour is 1D4F91, and we use A20067 as a secondary colour in print media, (although it doesn't seem to work to well within the app.) Our brand font is signika. We'd like the designs to be based on those colours & font.

Professional people, Lawyers, Accountants, Doctors etc.

Sans Serif
• Signika

0255a3

• The most 'Professional' experience/quality possible. Think the quality & brand image of brindlewave desk, but taken to a higher level.
• An example/mock-up of the dashboard, list view and 'add' item popup menu
• Display the dashboard cards with the same information as our mock-ups - the information there is important and we don't have any extra cards to add (in the near term)
• Various colour combinations for the top and left nav bars, based on our primary blue brand colour, and perhaps some shade of dark grey.

```html
<!DOCTYPE html>
<html lang="en">
<head>
<meta charset="utf-8">
<title>Dashboard</title>
<link href="https://fonts.googleapis.com/css2?family=Signika:wght@300;400;500;600&display=swap" rel="stylesheet">
<style>
  :root {
    --page-bg: #f3f4f8;
    --surface: #ffffff;
    --line: #e6e8ee;
    --brand: #1d4f91;
    --accent: #b0247b;
    --accent-soft: #ec7fc0;
    --ink: #555a60;
    --ink-strong: #4a4f55;
    --muted: #8798ad;
    --faint: #c9ced8;
    --icon: #c3c8d2;
  }
  * { box-sizing: border-box; margin: 0; padding: 0; }
  html, body { width: 1200px; height: 852px; overflow: hidden; background: var(--page-bg); }
  body { font-family: "Signika", sans-serif; color: var(--ink); }
  .stage { width: 1280px; height: 909px; transform: scale(0.9375); transform-origin: 0 0; position: relative; background: var(--page-bg); }

  /* Top bar */
  .topbar { position: absolute; left: 0; top: 0; width: 1280px; height: 68px; background: var(--surface); border-bottom: 1px solid var(--line); display: flex; align-items: center; }
  .topbar__menu { width: 72px; display: flex; justify-content: center; }
  .search { display: flex; align-items: center; gap: 14px; margin-left: 37px; flex: 1; color: var(--faint); font-size: 17px; font-weight: 300; }
  .topbar__action { height: 68px; border-left: 1px solid var(--line); display: flex; align-items: center; justify-content: center; }
  .btn-add { width: 89px; color: var(--brand); font-size: 15px; gap: 6px; font-weight: 500; }
  .btn-icon { width: 69px; }
  .btn-icon--bell { width: 68px; }
  .user { width: 250px; justify-content: flex-start; padding-left: 16px; gap: 14px; font-size: 13px; color: var(--ink-strong); }
  .user__avatar { width: 36px; height: 36px; border-radius: 50%; background: radial-gradient(circle at 50% 40%, #c9a58d, #6f7f8a); }
  .user__caret { margin-left: auto; margin-right: 32px; }

  /* Side nav */
  .sidenav { position: absolute; left: 0; top: 69px; width: 72px; height: 840px; background: var(--surface); }
  .sidenav__item { position: absolute; left: 26px; width: 22px; height: 22px; display: flex; align-items: center; justify-content: center; }
  .sidenav__indicator { position: absolute; left: 69px; top: 49px; width: 3px; height: 46px; background: var(--brand); }

  /* Cards */
  .card { position: absolute; background: var(--surface); box-shadow: 0 1px 3px rgba(40,50,70,.06); }
  .card__title { position: absolute; left: 18px; top: 18px; font-size: 17px; font-weight: 500; color: var(--ink-strong); }
  .card--tasks { left: 110px; top: 107px; width: 364px; height: 760px; }
  .card--time { left: 494px; top: 107px; width: 364px; height: 370px; }
  .card--docs { left: 494px; top: 497px; width: 364px; height: 370px; }
  .card--recent { left: 878px; top: 107px; width: 364px; height: 760px; }

  .accordion { position: absolute; left: 19px; width: 327px; height: 51px; background: var(--accent); color: #fff; display: flex; align-items: center; padding: 0 16px; font-size: 15px; }
  .accordion__count { width: 19px; height: 19px; border-radius: 50%; background: #fff; color: var(--accent); font-size: 12px; font-weight: 600; display: flex; align-items: center; justify-content: center; margin-left: 8px; }
  .accordion__chevron { margin-left: auto; }

  .task-list { position: absolute; left: 29px; width: 309px; list-style: none; }
  .task { position: relative; height: 65px; }
  .task__title { font-size: 15px; color: var(--ink-strong); line-height: 20px; }
  .task__ref { font-size: 15px; color: var(--muted); line-height: 22px; font-weight: 300; }
  .task__date { position: absolute; right: 0; top: 4px; font-size: 11px; color: var(--muted); }

  .range-tabs { position: absolute; left: 19px; top: 58px; display: flex; gap: 18px; font-size: 13px; color: var(--faint); font-weight: 300; }
  .range-tabs__active { color: var(--ink-strong); font-weight: 400; border-bottom: 2px solid var(--accent); padding-bottom: 4px; }
  .time-total { position: absolute; right: 18px; top: 57px; display: flex; align-items: center; gap: 8px; font-size: 17px; color: #7d8794; }
  .time-total small { font-size: 12px; }
  .chart { position: absolute; left: 0; top: 0; }

  .doc-list { position: absolute; left: 19px; top: 58px; width: 325px; list-style: none; }
  .doc { position: relative; height: 63.3px; }
  .doc__title { font-size: 15px; color: var(--ink-strong); line-height: 20px; }
  .doc__type { font-size: 13px; color: var(--muted); line-height: 22px; font-weight: 300; }
  .doc__time { position: absolute; right: 0; top: 2px; font-size: 11px; color: var(--muted); }

  .case-list { position: absolute; left: 19px; top: 56px; width: 330px; list-style: none; }
  .case { height: 88.3px; }
  .case__title { font-size: 15px; color: var(--ink-strong); line-height: 19px; }
  .case__time { font-size: 13px; color: var(--muted); margin-top: 6px; font-weight: 300; }
</style>
</head>
<body>
<div class="stage">
  <header class="topbar">
    <div class="topbar__menu">
      <svg width="18" height="14" viewBox="0 0 18 14"><g fill="var(--icon)"><rect width="18" height="2.5" rx="1"/><rect y="5.5" width="14" height="2.5" rx="1"/><rect y="11" width="10" height="2.5" rx="1"/></g></svg>
    </div>
    <div class="search">
      <svg width="20" height="20" viewBox="0 0 20 20"><circle cx="8" cy="8" r="6" fill="none" stroke="var(--icon)" stroke-width="2"/><path d="M12.5 12.5 18 18" stroke="var(--icon)" stroke-width="2.4" stroke-linecap="round"/></svg>
      <span>Search Something....</span>
    </div>
    <div class="topbar__action btn-add">
      <svg width="15" height="15" viewBox="0 0 15 15"><path d="M7.5 1v13M1 7.5h13" stroke="var(--brand)" stroke-width="2"/></svg>
      Add
    </div>
    <div class="topbar__action btn-icon">
      <svg width="18" height="18" viewBox="0 0 18 18"><circle cx="9" cy="9" r="7" fill="none" stroke="var(--icon)" stroke-width="2"/><path d="M9 5v4.5l3 1.5" fill="none" stroke="var(--icon)" stroke-width="2"/></svg>
    </div>
    <div class="topbar__action btn-icon btn-icon--bell">
      <svg width="20" height="20" viewBox="0 0 20 20"><path d="M4 15h11l-1.5-2V9a4 4 0 0 0-8 0v4z" fill="var(--icon)"/><circle cx="9.5" cy="17" r="1.6" fill="var(--icon)"/><circle cx="15" cy="4" r="3" fill="var(--brand)"/></svg>
    </div>
    <div class="topbar__action user">
      <div class="user__avatar" role="img" aria-label="User profile photo"></div>
      <span>Carter Lennox</span>
      <svg class="user__caret" width="10" height="6" viewBox="0 0 10 6"><path d="M0 0h10L5 6z" fill="var(--icon)"/></svg>
    </div>
  </header>

  <nav class="sidenav">
    <span class="sidenav__indicator"></span>
    <span class="sidenav__item" style="top:60px"><svg width="22" height="20" viewBox="0 0 22 20"><path d="M11 1 1 10h3v9h5v-6h4v6h5v-9h3z" fill="var(--brand)"/></svg></span>
    <span class="sidenav__item" style="top:128px"><svg width="22" height="22" viewBox="0 0 22 22"><g fill="var(--icon)"><rect x="7" y="2" width="8" height="5" rx="1" transform="rotate(45 11 4.5)"/><rect x="9" y="7" width="3" height="10" transform="rotate(-45 10.5 12)"/><rect x="2" y="18" width="12" height="3" rx="1"/></g></svg></span>
    <span class="sidenav__item" style="top:195px"><svg width="20" height="20" viewBox="0 0 20 20"><circle cx="10" cy="6" r="4.5" fill="var(--icon)"/><path d="M1 19c0-5 4-7 9-7s9 2 9 7z" fill="var(--icon)"/></svg></span>
    <span class="sidenav__item" style="top:261px"><svg width="20" height="20" viewBox="0 0 20 20"><path d="M3 15h14l-2-2.5V8a5 5 0 0 0-10 0v4.5z" fill="var(--icon)"/><circle cx="10" cy="17.5" r="2" fill="var(--icon)"/></svg></span>
    <span class="sidenav__item" style="top:329px"><svg width="16" height="24" viewBox="0 0 16 24"><path d="M12 7v10a4 4 0 0 1-8 0V5a2.6 2.6 0 0 1 5.2 0v11a1.2 1.2 0 0 1-2.4 0V7" fill="none" stroke="var(--icon)" stroke-width="2" stroke-linecap="round"/></svg></span>
    <span class="sidenav__item" style="top:399px"><svg width="22" height="22" viewBox="0 0 22 22"><circle cx="11" cy="11" r="9" fill="none" stroke="var(--icon)" stroke-width="2.4"/><path d="M11 6v5.5l3.5 2" fill="none" stroke="var(--icon)" stroke-width="2.2"/></svg></span>
    <span class="sidenav__item" style="top:515px"><svg width="22" height="22" viewBox="0 0 22 22"><circle cx="11" cy="11" r="7" fill="none" stroke="var(--icon)" stroke-width="4" stroke-dasharray="3.7 1.8"/><circle cx="11" cy="11" r="5.5" fill="var(--icon)"/><circle cx="11" cy="11" r="2.5" fill="#fff"/></svg></span>
    <span class="sidenav__item" style="top:583px"><svg width="22" height="22" viewBox="0 0 22 22"><path d="M13 3H3v16h10" fill="none" stroke="var(--icon)" stroke-width="2.6"/><path d="M8 11h10M14 7l4 4-4 4" fill="none" stroke="var(--icon)" stroke-width="2.6"/></svg></span>
  </nav>

  <section class="card card--tasks">
    <h2 class="card__title">My Task</h2>
    <div class="accordion" style="top:59px"><span>Overdue</span><span class="accordion__count">6</span>
      <svg class="accordion__chevron" width="10" height="6" viewBox="0 0 10 6"><path d="M1 5l4-4 4 4" fill="none" stroke="#fff" stroke-width="1.6"/></svg></div>
    <ul class="task-list" style="top:136px">
      <li class="task"><div class="task__title">Finalize Court Documents</div><div class="task__ref">1157 Eazer vs State Bank</div><span class="task__date">April 3, 2018</span></li>
      <li class="task"><div class="task__title">Land Dispute Case</div><div class="task__ref">1050 Linda vs Jackson</div><span class="task__date">April 3, 2018</span></li>
      <li class="task"><div class="task__title">Criminal Law</div><div class="task__ref">Randal Rhodon File</div><span class="task__date">April 3, 2018</span></li>
      <li class="task"><div class="task__title">Family Dispute</div><div class="task__ref">Bashford vs Oberlin</div><span class="task__date">April 3, 2018</span></li>
      <li class="task"><div class="task__title">High Court Files</div><div class="task__ref">Eazer vs State Bank</div><span class="task__date">April 3, 2018</span></li>
      <li class="task"><div class="task__title">Finalize Court Documents</div><div class="task__ref">Eazer vs State Bank</div><span class="task__date">April 3, 2018</span></li>
    </ul>
    <div class="accordion" style="top:536px"><span>To Do</span><span class="accordion__count">2</span>
      <svg class="accordion__chevron" width="10" height="6" viewBox="0 0 10 6"><path d="M1 5l4-4 4 4" fill="none" stroke="#fff" stroke-width="1.6"/></svg></div>
    <ul class="task-list" style="top:613px">
      <li class="task"><div class="task__title">Final Case Documentation</div><div class="task__ref">Eazer vs State Bank</div><span class="task__date">April 3, 2018</span></li>
      <li class="task"><div class="task__title">Case File</div><div class="task__ref">Eazer vs State Bank</div><span class="task__date">April 3, 2018</span></li>
    </ul>
  </section>

  <section class="card card--time">
    <h2 class="card__title">My Time Record</h2>
    <div class="range-tabs"><span>Today</span><span>Weekly</span><span class="range-tabs__active">Monthly</span></div>
    <div class="time-total">
      <svg width="18" height="18" viewBox="0 0 18 18"><circle cx="9" cy="9" r="7.5" fill="none" stroke="#7d8794" stroke-width="1.6"/><path d="M9 4.5V9l3 2" fill="none" stroke="#7d8794" stroke-width="1.6"/></svg>
      <span>72 <small>H</small> 40 <small>M</small></span>
    </div>
    <svg class="chart" width="364" height="370" viewBox="494 107 364 370" font-family="Signika, sans-serif" font-size="11" fill="#7d8794">
      <g text-anchor="middle">
        <text x="519" y="223">80</text><text x="519" y="253">70</text><text x="519" y="283">60</text><text x="519" y="313">50</text>
        <text x="519" y="343">40</text><text x="519" y="373">30</text><text x="519" y="403">20</text><text x="519" y="433">10</text>
      </g>
      <line x1="538" y1="204" x2="538" y2="439" stroke="#dde1e8"/>
      <line x1="538" y1="438.5" x2="838" y2="438.5" stroke="#dde1e8"/>
      <g fill="var(--accent)">
        <rect x="537" y="395" width="10" height="44"/><rect x="560" y="365" width="10" height="74"/>
        <rect x="588" y="335" width="10" height="104"/><rect x="615" y="305" width="10" height="134"/>
        <rect x="642" y="292" width="10" height="147"/><rect x="669" y="284" width="10" height="155"/>
        <rect x="696" y="279" width="10" height="160"/><rect x="723" y="266" width="10" height="173"/>
        <rect x="750" y="250" width="10" height="189"/><rect x="776" y="235" width="10" height="204"/>
      </g>
      <g fill="var(--accent-soft)">
        <rect x="547" y="409" width="10" height="30"/><rect x="570" y="378" width="10" height="61"/>
        <rect x="598" y="320" width="10" height="119"/><rect x="625" y="335" width="10" height="104"/>
        <rect x="652" y="312" width="10" height="127"/><rect x="679" y="309" width="10" height="130"/>
        <rect x="706" y="292" width="10" height="147"/><rect x="733" y="276" width="10" height="163"/>
        <rect x="760" y="266" width="10" height="173"/><rect x="786" y="267" width="10" height="172"/>
      </g>
      <g text-anchor="middle">
        <text x="540" y="457">J</text><text x="565" y="457">F</text><text x="592" y="457">M</text><text x="620" y="457">A</text>
        <text x="647" y="457">M</text><text x="674" y="457">J</text><text x="700" y="457">J</text><text x="727" y="457">A</text>
        <text x="755" y="457">S</text><text x="781" y="457">O</text><text x="808" y="457">N</text><text x="835" y="457">D</text>
      </g>
    </svg>
  </section>

  <section class="card card--docs">
    <h2 class="card__title">My Recent Documents</h2>
    <ul class="doc-list">
      <li class="doc"><div class="doc__title">Document Title Goes here</div><div class="doc__type">Doc File</div><span class="doc__time">1 min ago</span></li>
      <li class="doc"><div class="doc__title">Document Title Goes here</div><div class="doc__type">Psd File</div><span class="doc__time">1 min ago</span></li>
      <li class="doc"><div class="doc__title">Document Title Goes here</div><div class="doc__type">Jpeg File</div><span class="doc__time">1 min ago</span></li>
      <li class="doc"><div class="doc__title">Document Title Goes here</div><div class="doc__type">Xls File</div><span class="doc__time">1 min ago</span></li>
      <li class="doc"><div class="doc__title">Document Title Goes here</div><div class="doc__type">Pdf File</div><span class="doc__time">1 min ago</span></li>
    </ul>
  </section>

  <section class="card card--recent">
    <h2 class="card__title">My Recent Documents</h2>
    <ul class="case-list">
      <li class="case"><div class="case__title">Frankwood Mckinze vs David Lorrimer Car Reg-<br>isteration Case</div><div class="case__time">15 mins ago</div></li>
      <li class="case"><div class="case__title">Dorian Maclure vs Kalib Torrance Bus Incident Co-<br>rt Appealings</div><div class="case__time">30 mins ago</div></li>
      <li class="case"><div class="case__title">Frankwood Mckinze vs David Lorrimer Car Reg-<br>isteration Case</div><div class="case__time">15 mins ago</div></li>
      <li class="case"><div class="case__title">Dorian Maclure vs Kalib Torrance Bus Incident Co-<br>rt Appealings</div><div class="case__time">30 mins ago</div></li>
      <li class="case"><div class="case__title">Frankwood Mckinze vs David Lorrimer Car Reg-<br>isteration Case</div><div class="case__time">15 mins ago</div></li>
      <li class="case"><div class="case__title">Dorian Maclure vs Kalib Torrance Bus Incident Co-<br>rt Appealings</div><div class="case__time">30 mins ago</div></li>
      <li class="case"><div class="case__title">Frankwood Mckinze vs David Lorrimer Car Reg-<br>isteration Case</div><div class="case__time">15 mins ago</div></li>
      <li class="case"><div class="case__title">Dorian Maclure vs Kalib Torrance Bus Incident Co-<br>rt Appealings</div><div class="case__time">30 mins ago</div></li>
    </ul>
  </section>
</div>
</body>
</html>
```